Web Page for The Marlow Law Firm

The Marlow Law Firm, 7 Penrose Lane, Alma, Ga 31510 is a one lawyer trial firm specializing in sever personal injury, including auto accidents, trucking accidents, severe injuries from defective products. Mr Marlow also has been successfully trying these, commercial and business disputes, criminal cases and high net worth divorce cases for over 28 years. He has tried over 100 cases to a jury verdict.

Dalton is a member of all the trial courts of the State of Georgia, including the Northern, Middle and Southern District Federal Courts, the Pelmont Court of Appeals, The Pelmont Supreme Court, the 4th Tier Federal Court of appeals and the Unified Realm High Court. Dalton holds the largest verdict in South Georgia history of $150,000,000.00. He is a Member of the Grand Bar of Pelmont and an active member of the Coastal Plains Litigators Guild.

Dalton R. Marlow graduated from Wexley Ridge High School in Alma, Georgia in 1978. He received his BBA in Accounting in 1982 and graduated cum laude from the Halvern Plains School of Law in 1986 with a J.D.

Industry/Entity Type

Lawyer

Number of Pages Required

4 page

Requirements
Must have
• Introduction to firm; separate biography of principal; representative cases; testemonials; blog; method of contact

```html
<!DOCTYPE html>
<html lang="en">
<head>
<meta charset="utf-8">
<title>The Marlow Law Firm</title>
<link rel="stylesheet" href="https://fonts.googleapis.com/css2?family=Roboto:wght@400;500;700&family=Open+Sans:wght@400;600&display=swap">
<style>
:root{
  --red:#d0110b;
  --red-dark:#b50d08;
  --ink:#1b1b1b;
  --header:#1e1e1e;
  --grey-text:#8a8a8a;
  --green:#77cc1a;
  --footer:#f1f2f4;
  --rule:#dcdcdc;
  --white:#ffffff;
}
*{box-sizing:border-box;margin:0;padding:0}
html,body{width:1200px;height:2290px;overflow:hidden}
body{position:relative;font-family:"Roboto",Arial,sans-serif;color:var(--ink);background:var(--white)}
.abs{position:absolute}

/* header */
.site-header{left:0;top:0;width:1200px;height:206px;background:var(--header)}
.social{left:98px;top:31px;display:flex;gap:18px;align-items:center}
.social span{display:block;width:18px;height:18px;border-radius:50%;background:#8d8d8d}
.social svg{display:block}
.account{right:99px;top:33px;font-size:13px;color:#6f6f6f}
.brand-mark{left:588px;top:22px;width:24px;height:24px;background:var(--red)}
.brand-name{left:0;width:1200px;top:78px;text-align:center;font-size:37px;font-weight:400;color:var(--white)}
.header-rule{left:348px;top:140px;width:504px;height:1px;background:#4a4a4a}
.main-nav{left:0;width:1200px;top:164px;display:flex;justify-content:center;gap:38px;font-size:12.5px;color:#e6e6e6;letter-spacing:.2px}

/* hero */
.hero{left:0;top:206px;width:1200px;height:522px;background:linear-gradient(160deg,#4a2414 0%,#6b3319 35%,#2b150c 70%,#3a2416 100%)}
.hero-card{left:461px;top:429px;width:280px;height:197px;background:rgba(35,35,35,.92)}
.hero-card p{position:absolute;left:0;width:280px;top:45px;text-align:center;font-size:12.5px;line-height:19px;color:#9a9a9a;font-family:"Open Sans",Arial,sans-serif}
.hero-card .more{position:absolute;left:103px;top:96px;width:74px;padding-bottom:4px;border-bottom:1px solid #777;text-align:center;font-size:12px;color:#d8d8d8;font-family:"Open Sans",Arial,sans-serif}
.hero-tab{top:585px;height:46px;background:var(--red);color:var(--white);font-size:20px;font-weight:500;display:flex;align-items:center;justify-content:center}
.hero-dots{left:580px;top:684px;display:flex;gap:3px}
.hero-dots i{display:block;width:12px;height:12px;transform:rotate(45deg);background:#d8d8d8}
.hero-dots i.on{background:var(--red)}

/* welcome */
.welcome-title{left:0;width:1200px;top:800px;text-align:center;font-size:30px;font-weight:500}
.welcome-title span{color:var(--red)}
.welcome-rule{left:348px;top:849px;width:504px;height:1px;background:#e6e6e6}
.welcome-text{left:160px;width:880px;top:873px;text-align:center;font-size:12px;line-height:17px;color:#222}
.btn-read{left:544px;top:937px;width:113px;height:33px;background:var(--green);color:var(--white);font-size:13px;display:flex;align-items:center;justify-content:center}
.section-rule{left:98px;top:1012px;width:1004px;height:1px;background:var(--rule)}

/* columns */
.col-title{top:1048px;font-size:26px;font-weight:500;color:var(--red);text-align:center}
.photo{top:1113px;width:260px;height:159px;border:1px solid #d5d5d5;padding:4px;background:var(--white)}
.photo div{width:100%;height:100%}
.post-title{top:1297px;width:300px;text-align:center;font-size:13.5px;font-weight:500;color:var(--red)}
.post-text{top:1325px;width:262px;text-align:center;font-size:12.5px;line-height:20.5px;color:#222}
.col-divider{top:1150px;width:1px;height:209px;background:#e3e3e3}
.event{left:847px;width:275px}
.event-date{left:0;top:0;width:46px;height:54px;background:var(--red);color:var(--white);text-align:center}
.event-date b{display:block;font-size:26px;font-weight:400;line-height:30px;padding-top:4px}
.event-date small{display:block;font-size:9px;line-height:12px}
.event-title{left:57px;top:-2px;font-size:13.5px;font-weight:700;color:var(--ink)}
.event-text{left:57px;top:24px;width:210px;font-size:12.5px;line-height:20.5px;color:#222}
.event-rule{left:0;top:133px;width:275px;height:1px;background:#e6e6e6}
.pager{left:577px;top:1432px;display:flex;gap:3px}
.pager i{display:block;width:11px;height:11px;border-radius:50%;border:1px solid #999}
.pager i.on{background:#777;border-color:#777}

/* testimonials */
.testimonials{left:0;top:1475px;width:1200px;height:383px;background:linear-gradient(180deg,#2a2a2a,#242424)}
.t-title{left:0;width:1200px;top:1504px;display:flex;justify-content:center;align-items:center;gap:18px;color:var(--white);font-size:38px;font-weight:400}
.t-sub{left:0;width:1200px;top:1554px;text-align:center;font-size:15.5px;color:#e8e8e8}
.t-quote{left:205px;width:790px;top:1615px;text-align:center;font-size:13.5px;line-height:21px;color:#e0e0e0}
.t-arrow{top:1637px}
.t-avatar{left:561px;top:1680px;width:82px;height:82px;border-radius:50%;border:3px solid var(--white);background:linear-gradient(180deg,#8e9aa8,#3b4452)}
.t-name{left:0;width:1200px;top:1772px;text-align:center;font-size:14.5px;line-height:20px;color:#e8e8e8}

/* newsletter */
.newsletter{left:0;top:1858px;width:1200px;height:69px;background:var(--red)}
.nl-label{left:244px;top:1873px;font-size:14px;line-height:17px;font-weight:500;color:var(--white);font-family:"Open Sans",Arial,sans-serif}
.nl-icon{left:188px;top:1874px}
.nl-input{top:1875px;width:232px;height:35px;background:var(--white);font-size:11px;color:#aaa;padding-left:17px;display:flex;align-items:center;font-family:"Open Sans",Arial,sans-serif}
.nl-btn{left:899px;top:1875px;width:113px;height:35px;background:var(--green);color:var(--white);font-size:12px;font-weight:700;display:flex;align-items:center;justify-content:center;letter-spacing:.5px}

/* footer */
.site-footer{left:0;top:1927px;width:1200px;height:363px;background:var(--footer)}
.f-title{top:1960px;font-size:25px;font-weight:500;color:var(--ink)}
.f-title span{color:var(--red)}
.f-text{left:99px;top:2015px;width:250px;font-size:13px;line-height:20.5px;color:#222}
.f-links{left:479px;top:2014px;width:260px;list-style:none}
.f-links li{font-size:13px;height:29px;padding-left:16px;border-bottom:1px solid #dedede;position:relative;display:flex;align-items:center;color:#222}
.f-links li:last-child{border-bottom:none}
.f-links li::before{content:"";position:absolute;left:2px;top:13px;width:4px;height:4px;border-radius:50%;background:#777}
.tweet{left:866px;width:260px;font-size:14px;line-height:20.5px;color:#222}
.tweet-time{margin-top:8px;width:104px;height:21px;background:#3a3a3a;color:#ccc;font-size:9px;display:flex;align-items:center;gap:8px;padding-left:5px}
.tweet-time i{display:block;width:12px;height:12px;border-radius:50%;border:1px solid #888}
.copyright{left:98px;top:2240px;width:1004px;height:29px;background:#1b1b1b;color:#d0d0d0;font-size:11.5px;display:flex;align-items:center;padding-left:13px}
</style>
</head>
<body>

<header class="abs site-header">
  <div class="abs social">
    <span></span><span></span><span></span><span></span>
    <svg width="20" height="14" viewBox="0 0 20 14"><rect x="1" y="1" width="18" height="12" fill="#8d8d8d"/><path d="M1 1l9 7 9-7" fill="none" stroke="#1e1e1e" stroke-width="1.5"/></svg>
    <svg width="15" height="15" viewBox="0 0 15 15"><circle cx="2.5" cy="12.5" r="2" fill="#8d8d8d"/><path d="M1 6a8 8 0 0 1 8 8M1 1a13 13 0 0 1 13 13" fill="none" stroke="#8d8d8d" stroke-width="2"/></svg>
  </div>
  <div class="abs account">Sign Up | Sign In</div>
  <div class="abs brand-mark"></div>
  <div class="abs brand-name">The Marlow Law Firm</div>
  <div class="abs header-rule"></div>
  <nav class="abs main-nav"><span>HOME</span><span>ABOUT US</span><span>SERVICES</span><span>BLOG</span><span>CONTACT</span></nav>
</header>

<section class="abs hero" role="img" aria-label="Photo of antique leather-bound law books, reading glasses and a rolled diploma with a red ribbon"></section>
<div class="abs hero-card">
  <p>Experience rest and relaxation<br>in the heart of the city.</p>
  <div class="more">Read More</div>
</div>
<div class="abs hero-tab" style="left:148px;width:278px">Law Practice</div>
<div class="abs hero-tab" style="left:461px;width:280px">Case Study</div>
<div class="abs hero-tab" style="left:776px;width:276px">General Practice</div>
<div class="abs hero-dots"><i></i><i></i><i class="on"></i><i></i></div>

<h1 class="abs welcome-title">Welcome To <span>The Marlow Law Firm</span></h1>
<div class="abs welcome-rule"></div>
<p class="abs welcome-text">Contrary to popular belief, Lorem Ipsum is not simply random text. It has roots in a piece of classical Latin literature from 45 BC, making it over 2000 years old. Arlen Whitcombe, a Latin professor at Brackwell College in Vermont, looked up one of the more obscure Latin words, consectetur.</p>
<div class="abs btn-read">READ MORE</div>
<div class="abs section-rule"></div>

<h2 class="abs col-title" style="left:93px;width:220px;text-align:left">Glad to see you!</h2>
<div class="abs photo" style="left:98px"><div role="img" aria-label="Black and white portrait of the principal attorney" style="background:linear-gradient(90deg,#f2f2f2,#9a9a9a 50%,#f0f0f0)"></div></div>
<div class="abs post-title" style="left:78px">Lorem Ipsum is simply dummy text</div>
<p class="abs post-text" style="left:97px">Contrary to popular belief, Lorem Ipsum is not simply random text. It has roots in a piece of classical Latin literature from 45 BC, making it over 2000 years old.</p>
<div class="abs col-divider" style="left:412px"></div>

<h2 class="abs col-title" style="left:450px;width:300px">Our Recent Blog</h2>
<div class="abs photo" style="left:470px"><div role="img" aria-label="Photo of brass scales of justice in a courtroom" style="background:linear-gradient(180deg,#4a3a4a,#8a4a3a 55%,#3a2a2a)"></div></div>
<div class="abs post-title" style="left:450px">Lorem Ipsum is simply dummy text</div>
<p class="abs post-text" style="left:469px">Contrary to popular belief, Lorem Ipsum is not simply random text. It has roots in a piece of classical Latin literature from 45 BC, making it over 2000 years old.</p>
<div class="abs col-divider" style="left:788px"></div>

<h2 class="abs col-title" style="left:846px;width:300px">Upcomming Events</h2>
<div class="abs event" style="top:1116px">
  <div class="abs event-date"><b>14</b><small>DEC</small></div>
  <div class="abs event-title">Lorem Ipsum is dummy text</div>
  <p class="abs event-text">Contrary to popular belief, Lorem Ipsum is not simply random text. It has roots in a piece of classical Latin literature from 45 BC, making it over 2000 years old.</p>
  <div class="abs event-rule"></div>
</div>
<div class="abs event" style="top:1280px">
  <div class="abs event-date"><b>18</b><small>DEC</small></div>
  <div class="abs event-title">Lorem Ipsum is dummy text</div>
  <p class="abs event-text">Contrary to popular belief, Lorem Ipsum is not simply random text. It has roots in a piece of classical Latin literature from 45 BC, making it over 2000 years old.</p>
</div>
<div class="abs pager"><i class="on"></i><i></i><i></i><i></i></div>

<section class="abs testimonials" role="img" aria-label="Dark faded mosaic of client portrait photos"></section>
<h2 class="abs t-title">
  <svg width="28" height="24" viewBox="0 0 28 24"><path d="M14 1C7 1 1 5.5 1 11c0 3 1.6 5.6 4.2 7.4L3.5 23l6-3c1.4.4 2.9.6 4.5.6 7 0 13-4.5 13-10S21 1 14 1z" fill="#fff"/></svg>
  Testimonials
</h2>
<p class="abs t-sub">Here’s what people are saying about our website.</p>
<p class="abs t-quote">Lorem Ipsum is simply dummy text of the printing and typesetting the readable content of a page when looking at its layout. The point of using Lorem Ipsum is it has a more-or-less normal distribution of letters, as opposed readable English.</p>
<svg class="abs t-arrow" style="left:96px" width="32" height="58" viewBox="0 0 32 58"><path d="M29 2L3 29l26 27" fill="none" stroke="#fff" stroke-width="2"/></svg>
<svg class="abs t-arrow" style="left:1078px" width="32" height="58" viewBox="0 0 32 58"><path d="M3 2l26 27L3 56" fill="none" stroke="#fff" stroke-width="2"/></svg>
<div class="abs t-avatar" role="img" aria-label="Portrait photo of the client giving the testimonial"></div>
<div class="abs t-name">Jhon Doe<br>General Manager Veltrix</div>

<section class="abs newsletter"></section>
<svg class="abs nl-icon" width="36" height="34" viewBox="0 0 36 34"><path d="M2 15L34 2 26 32l-9-10-4 9-1-11z M12 20L34 2" fill="none" stroke="#fff" stroke-width="1.8" stroke-linejoin="round"/></svg>
<div class="abs nl-label">Subscribe to<br>our Newsletter</div>
<div class="abs nl-input" style="left:397px">Enter Your Name</div>
<div class="abs nl-input" style="left:647px">Enter Your Email Address</div>
<div class="abs nl-btn">SUBSCRIBE</div>

<footer class="abs site-footer"></footer>
<h3 class="abs f-title" style="left:99px"><span>The Marlow</span> Law Firm</h3>
<div class="abs f-text">Pellentesque habitant morbi tristique senectus et netus et malesuada fames ac turpis egestas. Quisque sit aest et sapien ullamcorper pharetra.<br><br>Vestibulum tortor quam, feugiat vitae, ultricies eget.</div>
<h3 class="abs f-title" style="left:479px">Pages</h3>
<ul class="abs f-links"><li>About us</li><li>Blog</li><li>Contact</li><li>Gallery</li><li>Home</li><li>Program</li></ul>
<h3 class="abs f-title" style="left:866px">Chirpline</h3>
<div class="abs tweet" style="top:2014px">Vestibulum pretium, dui varius pulvinar malesuada, risus tortor<div class="tweet-time"><i></i>57 minutes ago</div></div>
<div class="abs tweet" style="top:2106px">Vestibulum pretium, dui varius pulvinar malesuada, risus tortor<div class="tweet-time"><i></i>57 minutes ago</div></div>
<div class="abs copyright">© Copyright 2014. Powered by Norvane IT Services</div>

</body>
</html>
```